Brixtondel - eCommerce Design and Shopify Theme customisation

eCommerce Website Design - firstly with mockups then once we have chosen the design the successful designer will need to choose, purchase and customise a Shopify theme to match the design. We have a logo already designed and now want to create our web presence based on carrying up to 50 products on our website.
Target Market(s)
UK Pet Owners
Industry/Entity Type
Pet Shop
Requirements
Must have
- Design must be achievable using a customised Shopify theme - the successful designer will be responsible for the delivery of a working theme on our shopify website.
Should not have
- should not look cheap or have designs that aren't compatible or achievable with Shopify

```html
<!DOCTYPE html>
<html lang="en">
<head>
<meta charset="utf-8">
<title>Brixtondel — Pet Shop</title>
<link rel="stylesheet" href="https://fonts.googleapis.com/css2?family=Montserrat:wght@400;500;600;700&display=swap">
<style>
  :root {
    --brand-yellow: #fdc11a;
    --ink: #2b2b2b;
    --white: #ffffff;
    --hero-green: #5f8a3c;
    --hero-brown: #7a4a24;
    --hero-dark: #2d2a22;
    --pet-tan: #c8a070;
  }
  * { box-sizing: border-box; margin: 0; padding: 0; }
  html, body {
    width: 1200px; height: 1200px; overflow: hidden;
    background: var(--white);
    font-family: "Montserrat", sans-serif;
    color: var(--ink);
  }
  .page { position: relative; width: 1200px; height: 1200px; }

  .promo-bar {
    position: absolute; top: 0; left: 0; width: 1200px; height: 30px;
    background: var(--brand-yellow); color: var(--white);
    font-size: 7.5px; font-weight: 700; letter-spacing: 0.2px;
    display: flex; align-items: center; justify-content: space-between;
    padding: 0 26px;
  }
  .promo-links { display: flex; gap: 15px; }

  .site-header { position: absolute; top: 30px; left: 0; width: 1200px; height: 123px; }
  .nav-link {
    position: absolute; top: 53px;
    font-size: 10px; font-weight: 600; letter-spacing: 1.2px;
    text-transform: uppercase; color: var(--ink);
  }
  .search { left: 27px; display: flex; align-items: center; gap: 8px; top: 50px; }
  .search svg { width: 16px; height: 16px; }
  .cart { left: 1098px; display: flex; align-items: center; gap: 8px; top: 48px; }
  .cart-badge {
    width: 16px; height: 16px; border-radius: 50%;
    background: var(--brand-yellow); color: var(--white);
    font-size: 8px; display: flex; align-items: center; justify-content: center;
  }
  .brand {
    position: absolute; left: 500px; width: 200px; top: 22px;
    display: flex; flex-direction: column; align-items: center; gap: 10px;
  }
  .brand-dot { width: 44px; height: 44px; border-radius: 50%; background: var(--brand-yellow); }
  .brand-name { font-size: 26px; font-weight: 500; color: var(--ink); letter-spacing: -0.5px; }

  .hero {
    position: absolute; top: 153px; left: 0; width: 1200px; height: 600px;
    background:
      radial-gradient(ellipse 300px 360px at 640px 330px, var(--hero-brown) 0%, #5a3a20 55%, transparent 80%),
      linear-gradient(180deg, #a59e8e 0%, #8a9274 22%, var(--hero-green) 50%, #3f5e2b 85%, var(--hero-dark) 100%);
  }
  .hero-copy {
    position: absolute; top: 245px; left: 0; width: 1200px; text-align: center; color: var(--white);
  }
  .hero-title {
    font-size: 37px; font-weight: 600; letter-spacing: 2px; text-transform: uppercase;
    text-shadow: 0 2px 6px rgba(0,0,0,0.35);
  }
  .hero-sub { margin-top: 12px; font-size: 18px; font-weight: 400; letter-spacing: 0.4px; }
  .btn-shop {
    display: inline-block; margin-top: 28px; width: 165px; height: 34px; line-height: 34px;
    background: var(--brand-yellow); color: var(--white);
    font-size: 10.5px; font-weight: 600; letter-spacing: 1.5px; text-transform: uppercase;
  }

  .products { position: absolute; top: 815px; left: 0; width: 1200px; text-align: center; }
  .products-title { font-size: 40px; font-weight: 400; letter-spacing: 1.5px; }
  .products-sub { margin-top: 14px; font-size: 14px; font-weight: 400; }
  .products-visual {
    position: absolute; left: 424px; top: 105px; width: 360px; height: 252px;
    background: radial-gradient(ellipse at 60% 55%, #e8d6b4 0%, var(--pet-tan) 45%, rgba(255,255,255,0) 75%);
  }
</style>
</head>
<body>
<div class="page">
  <div class="promo-bar">
    <span>FREE SHIPPING WHEN YOU SPEND £36 OR MORE</span>
    <span class="promo-links"><span>MY ACCOUNT</span><span>LOGIN</span><span>1-800-5550-0199</span></span>
  </div>

  <header class="site-header">
    <a class="nav-link search">
      <svg viewBox="0 0 16 16" fill="none" stroke="#2b2b2b" stroke-width="2"><circle cx="6.5" cy="6.5" r="5"/><line x1="10.2" y1="10.2" x2="15" y2="15"/></svg>
      Search
    </a>
    <a class="nav-link" style="left:326px">Home</a>
    <a class="nav-link" style="left:381px">Dogs</a>
    <a class="nav-link" style="left:434px">Cats</a>
    <div class="brand">
      <span class="brand-dot"></span>
      <span class="brand-name">Brixtondel</span>
    </div>
    <a class="nav-link" style="left:738px">Shop</a>
    <a class="nav-link" style="left:793px">Blog</a>
    <a class="nav-link" style="left:846px">Contact Us</a>
    <a class="nav-link cart">
      <svg width="16" height="18" viewBox="0 0 16 18" fill="none" stroke="#2b2b2b" stroke-width="1.6"><rect x="1" y="5" width="14" height="12"/><path d="M5 7V3a3 3 0 0 1 6 0v4"/></svg>
      Cart <span class="cart-badge">2</span>
    </a>
  </header>

  <section class="hero" role="img" aria-label="Photo of a German Shepherd dog in a green field">
    <div class="hero-copy">
      <h1 class="hero-title">Our Pets Deserves The Best</h1>
      <p class="hero-sub">Treat them to the good stuffs</p>
      <a class="btn-shop">Shop Now</a>
    </div>
  </section>

  <section class="products">
    <h2 class="products-title">Our Products</h2>
    <p class="products-sub">Treat them to the good stuffs</p>
    <div class="products-visual" role="img" aria-label="Photo of a tabby cat lying beside a sitting Labrador puppy"></div>
  </section>
</div>
</body>
</html>
```